Velmarcoteni Business cards

Dear team, I need to get the design file to suit it to our team. The focus of the business card is the Automotive Market and the design must be in black colour and the logo must be in glossy black. On the front of the card I need to get the following info:

- Name and Surname
- Title
- eMail
- Phone Number
- Skype account
- domain address

```html
<!DOCTYPE html>
<html lang="en">
<head>
<meta charset="utf-8">
<title>Velmarcoteni Business Cards</title>
<link rel="stylesheet" href="https://fonts.googleapis.com/css2?family=Montserrat:wght@700;800&family=Open+Sans:wght@400;600&display=swap">
<style>
  :root {
    --stage: #3a3330;
    --card: #161616;
    --card-edge: #0d0d0d;
    --accent: #e3202a;
    --ink: #f2f2f2;
    --pattern-dark: #1a1a1a;
    --pattern-light: #8d8d8d;
  }
  * { margin: 0; padding: 0; box-sizing: border-box; }
  html, body { width: 1200px; height: 716px; overflow: hidden; }
  body {
    background: var(--stage);
    display: flex;
    align-items: center;
    justify-content: center;
    gap: 40px;
    font-family: "Open Sans", sans-serif;
  }
  .card {
    position: relative;
    width: 520px;
    height: 298px;
    background: var(--card);
    border-radius: 4px;
    overflow: hidden;
    box-shadow: 0 14px 30px rgba(0,0,0,.45);
  }
  .card--back { border-bottom: 6px solid var(--accent); }
  .pattern-field {
    position: absolute;
    inset: 0;
    background: linear-gradient(110deg, var(--pattern-dark) 0%, var(--pattern-dark) 40%, var(--pattern-light) 85%, #a8a8a8 100%);
  }
  .pattern-highlight {
    position: absolute;
    left: 322px;
    top: 196px;
    width: 40px;
    height: 40px;
    background: var(--accent);
  }
  .brand {
    position: absolute;
    left: 30px;
    top: 34px;
    display: flex;
    align-items: center;
    gap: 10px;
  }
  .brand-mark {
    width: 26px;
    height: 26px;
    background: var(--accent);
  }
  .brand-name {
    font-family: "Montserrat", sans-serif;
    font-weight: 800;
    font-size: 24px;
    color: var(--ink);
    letter-spacing: .2px;
  }
  .person {
    position: absolute;
    right: 30px;
    top: 112px;
    text-align: right;
  }
  .person-name {
    font-family: "Montserrat", sans-serif;
    font-weight: 800;
    font-size: 22px;
    color: var(--accent);
    letter-spacing: .5px;
    text-transform: uppercase;
  }
  .person-title {
    font-size: 13px;
    color: var(--ink);
    margin-top: 2px;
  }
  .contacts {
    position: absolute;
    left: 30px;
    bottom: 30px;
    list-style: none;
  }
  .contact {
    display: flex;
    align-items: center;
    gap: 7px;
    font-size: 12.5px;
    line-height: 19px;
    color: var(--ink);
  }
  .contact svg { width: 10px; height: 10px; fill: var(--accent); flex: none; }
  .address {
    position: absolute;
    right: 30px;
    bottom: 30px;
    text-align: right;
    font-size: 13.5px;
    line-height: 19px;
    color: var(--ink);
    font-style: normal;
  }
</style>
</head>
<body>
  <section class="card card--back">
    <div class="pattern-field" role="img" aria-label="Repeating brand symbol pattern in glossy black fading to silver"></div>
    <div class="pattern-highlight"></div>
  </section>

  <section class="card card--front">
    <div class="brand">
      <span class="brand-mark"></span>
      <span class="brand-name">Velmarcoteni.com</span>
    </div>

    <div class="person">
      <div class="person-name">Darel Quinby</div>
      <div class="person-title">Director</div>
    </div>

    <ul class="contacts">
      <li class="contact">
        <svg viewBox="0 0 10 10"><path d="M2 0.5 L3.6 0.5 L4.3 2.8 L3.2 3.7 Q4.1 5.9 6.3 6.8 L7.2 5.7 L9.5 6.4 L9.5 8 Q9.5 9.5 8 9.5 Q0.5 9 0.5 2 Q0.5 0.5 2 0.5 Z"/></svg>
        555-014-2270
      </li>
      <li class="contact">
        <svg viewBox="0 0 10 10"><path d="M0 1.5 H10 V8.5 H0 Z M0.8 2.2 L5 5.4 L9.2 2.2" fill="var(--accent)"/><path d="M0.8 2.2 L5 5.4 L9.2 2.2" stroke="#161616" stroke-width="1" fill="none"/></svg>
        info@velmarcoteni.com
      </li>
      <li class="contact">
        <svg viewBox="0 0 10 10"><circle cx="5" cy="5" r="4.5"/></svg>
        velmarcoteni
      </li>
    </ul>

    <address class="address">
      2187 W Ordell, Brannock,<br>
      Kansas 60412
    </address>
  </section>
</body>
</html>
```